Steady Pathways, Inc
Steady Pathways
Bright & Fun-filled
Marisa Delacorte
P.O. Box 38216
4873-B Thimble Crest Road
Goldsboro, NC 27845
madelacorte@steadypathwaysgrp.net
"Press Toward The Mark A+"
Logo File.

```html
<!DOCTYPE html>
<html lang="en">
<head>
<meta charset="utf-8">
<title>Steady Pathways, Inc — Stationery Set</title>
<link href="https://fonts.googleapis.com/css2?family=Poppins:wght@400;600&display=swap" rel="stylesheet">
<style>
  :root {
    --navy: #2b2a8e;
    --red: #e5263a;
    --paper: #ffffff;
    --backdrop: #efe8dc;
    --caption: #7a6f60;
    --ink: #3a3a4a;
    --font: "Poppins", Arial, sans-serif;
  }
  html, body { margin: 0; padding: 0; }
  body {
    width: 1200px; height: 346px; overflow: hidden;
    background: var(--backdrop); position: relative; font-family: var(--font);
  }
  .piece { position: absolute; background: var(--paper); box-shadow: 0 1px 3px rgba(0,0,0,.25); overflow: hidden; }
  .piece svg.art { position: absolute; inset: 0; width: 100%; height: 100%; }
  .caption {
    position: absolute; font-size: 5px; letter-spacing: .4px; color: var(--caption);
    text-transform: uppercase; white-space: nowrap; transform: translateX(-50%);
  }
  .brand { position: absolute; display: flex; align-items: center; gap: 3px; color: var(--navy); font-weight: 600; line-height: 1; white-space: nowrap; }
  .brand .dot { border-radius: 50%; background: var(--red); flex: none; }
  .contact { position: absolute; font-size: 3.4px; line-height: 1.5; color: var(--ink); }
  .motto { position: absolute; font-size: 4px; color: var(--red); font-weight: 600; }
  .faint-circle { position: absolute; border-radius: 50%; background: radial-gradient(circle, rgba(229,38,58,.08), rgba(43,42,142,.06) 60%, transparent 70%); }

  .card-front { left: 8px; top: 170px; width: 100px; height: 56px; }
  .card-back  { left: 8px; top: 236px; width: 100px; height: 56px; }
  .letterhead-one { left: 132px; top: 18px; width: 205px; height: 300px; }
  .letterhead-two { left: 372px; top: 18px; width: 215px; height: 305px; }
  .envelope-one { left: 619px; top: 44px; width: 198px; height: 88px; }
  .envelope-two { left: 619px; top: 170px; width: 198px; height: 92px; }
  .envelope-back { left: 962px; top: 38px; width: 230px; height: 238px; }
</style>
</head>
<body>

  <!-- Business card front -->
  <div class="piece card-front">
    <svg class="art" viewBox="0 0 100 56" preserveAspectRatio="none">
      <path d="M0 46 Q50 30 100 40 L100 56 L0 56Z" fill="var(--navy)"/>
      <path d="M0 44 Q50 28 100 38 L100 40 Q50 30 0 46Z" fill="var(--red)"/>
    </svg>
    <div class="brand" style="left:6px;top:7px;font-size:6px"><span class="dot" style="width:5px;height:5px"></span>Steady Pathways</div>
    <div class="contact" style="left:6px;top:18px;font-size:3px">Marisa Delacorte<br>madelacorte@steadypathwaysgrp.net</div>
  </div>
  <span class="caption" style="left:58px;top:228px">Business Card Front</span>

  <!-- Business card back -->
  <div class="piece card-back">
    <div class="contact" style="left:10px;top:18px;font-size:4px">"Press Toward The Mark</div>
    <div class="motto" style="left:10px;top:26px;font-size:6px">A+"</div>
  </div>
  <span class="caption" style="left:58px;top:294px">Business Card Back</span>

  <!-- Letterhead option 1 -->
  <div class="piece letterhead-one">
    <svg class="art" viewBox="0 0 205 300" preserveAspectRatio="none">
      <path d="M0 262 Q100 232 205 248 L205 300 L0 300Z" fill="var(--navy)"/>
      <path d="M0 256 Q100 224 205 240 L205 248 Q100 232 0 262Z" fill="var(--red)"/>
    </svg>
    <div class="brand" style="left:12px;top:12px;font-size:11px"><span class="dot" style="width:8px;height:8px"></span>Steady Pathways</div>
    <div class="contact" style="left:30px;top:27px">P.O. Box 38216 · Goldsboro, NC 27845</div>
    <div class="faint-circle" style="left:72px;top:200px;width:60px;height:60px"></div>
  </div>
  <span class="caption" style="left:234px;top:322px">Letterhead Option 1</span>

  <!-- Letterhead option 2 -->
  <div class="piece letterhead-two">
    <svg class="art" viewBox="0 0 215 305" preserveAspectRatio="none">
      <path d="M0 0 L215 0 L215 14 Q110 6 0 24Z" fill="var(--navy)"/>
      <path d="M0 24 Q110 6 215 14 L215 18 Q110 10 0 28Z" fill="var(--red)"/>
      <path d="M0 290 Q110 276 215 282 L215 305 L0 305Z" fill="var(--navy)"/>
    </svg>
    <div class="brand" style="left:50%;transform:translateX(-50%);top:34px;font-size:11px"><span class="dot" style="width:8px;height:8px"></span>Steady Pathways</div>
    <div class="contact" style="left:0;right:0;text-align:center;top:49px">4873-B Thimble Crest Road · Goldsboro, NC 27845</div>
    <div class="faint-circle" style="left:72px;top:120px;width:72px;height:72px"></div>
  </div>
  <span class="caption" style="left:480px;top:327px">Letterhead Option 2</span>

  <!-- Envelope option 1 -->
  <div class="piece envelope-one">
    <svg class="art" viewBox="0 0 198 88" preserveAspectRatio="none">
      <path d="M0 0 L70 0 Q40 14 0 30Z" fill="var(--navy)"/>
      <path d="M70 0 L80 0 Q45 16 0 34 L0 30 Q40 14 70 0Z" fill="var(--red)"/>
    </svg>
    <div class="brand" style="left:28px;top:8px;font-size:8px"><span class="dot" style="width:6px;height:6px"></span>Steady Pathways</div>
    <div class="contact" style="left:40px;top:20px">P.O. Box 38216 · Goldsboro, NC 27845</div>
  </div>
  <span class="caption" style="left:718px;top:135px">Envelope Option 1</span>

  <!-- Envelope option 2 -->
  <div class="piece envelope-two">
    <svg class="art" viewBox="0 0 198 92" preserveAspectRatio="none">
      <path d="M0 0 L198 0 L198 6 Q100 2 0 18Z" fill="var(--navy)"/>
      <path d="M0 18 Q100 2 198 6 L198 9 Q100 5 0 21Z" fill="var(--red)"/>
      <path d="M0 82 Q100 74 198 78 L198 92 L0 92Z" fill="var(--navy)"/>
    </svg>
    <div class="brand" style="left:10px;top:24px;font-size:8px"><span class="dot" style="width:6px;height:6px"></span>Steady Pathways</div>
    <div class="contact" style="left:22px;top:35px">4873-B Thimble Crest Road</div>
    <div class="faint-circle" style="left:80px;top:40px;width:38px;height:38px"></div>
  </div>
  <span class="caption" style="left:718px;top:265px">Envelope Option 2</span>

  <!-- Envelope back flap -->
  <div class="piece envelope-back">
    <svg class="art" viewBox="0 0 230 238" preserveAspectRatio="none">
      <path d="M0 0 L230 0 L230 40 Q115 62 0 40Z" fill="var(--navy)"/>
      <path d="M0 72 Q115 46 230 72 L230 124 Q115 98 0 124Z" fill="var(--red)"/>
      <path d="M0 124 Q115 98 230 124 L230 238 L0 238Z" fill="var(--paper)"/>
      <path d="M0 124 L115 176 L230 124" fill="none" stroke="#d8d8e0" stroke-width="1"/>
      <path d="M0 238 L90 170 M230 238 L140 170" fill="none" stroke="#e4e4ea" stroke-width="1"/>
    </svg>
  </div>
  <span class="caption" style="left:1077px;top:280px">Envelope Back Flap</span>

</body>
</html>
```